Birchwell Landing - Multifamily Development

Birchwell Landing is a Luxury Multifamily Development project located in Orange, NJ. This project will be completed in three phases with the first phase about 75% complete. Each phase will have a different name as follows
CREST Birchwell Landing
RIDGE Birchwell Landing
ZENITHAL Birchwell Landing
We are going to install a banner on the side of the first building which will act as advertising for all buildings. We will eventually need advertising that will be in the windows as well as marketing materials . We want the marketing for this project to be similar for all three phases. At the moment, we are starting with this first simple banner. Attached is a rough idea of the look as well as our color palette. If you feel the color palette is a little too monochrome, feel free to propose an accent color. You can also visit our website to see more info on our company as well as the project. www.tolvarhq.com Finally, if you need AI files (ie. for the logo), we can send to you. Thanks..

```html
<!DOCTYPE html>
<html lang="en">
<head>
<meta charset="utf-8">
<title>Crest Birchwell Landing – New Apartments</title>
<link href="https://fonts.googleapis.com/css2?family=Prata&family=Playfair+Display:wght@500;600&family=Poppins:wght@300&family=Montserrat:wght@700&display=swap" rel="stylesheet">
<style>
  :root {
    --violet-deep: #433b79;
    --violet-mid: #6a639a;
    --violet-soft: #b6b1d2;
    --cream: #f8f8ec;
    --white: #ffffff;
    --ink: #2b2a30;
    --brand-violet: #4a4283;
    --render-light: #c9a98c;
    --render-mid: #9a6a52;
    --render-dark: #46464c;
  }
  * { margin: 0; padding: 0; box-sizing: border-box; }
  html, body { width: 848px; height: 1200px; overflow: hidden; background: var(--violet-deep); }
  .banner {
    position: relative;
    width: 848px;
    height: 1200px;
    overflow: hidden;
    background:
      radial-gradient(ellipse 70% 45% at 50% 78%, var(--violet-soft) 0%, rgba(182,177,210,0) 100%),
      linear-gradient(180deg, var(--violet-deep) 0%, #5a5390 35%, var(--violet-mid) 55%, #a39ec6 80%);
  }
  .phase-mark {
    position: absolute;
    left: 284px; top: 0;
    width: 310px; height: 129px;
    background: var(--white);
    display: flex; align-items: center; justify-content: center;
  }
  .phase-name {
    font-family: "Prata", serif;
    font-size: 92px;
    line-height: 1;
    color: var(--brand-violet);
    margin-top: -6px;
  }
  .project-name {
    position: absolute;
    left: 162px; top: 130px;
    width: 600px;
    text-align: center;
    font-family: "Poppins", sans-serif;
    font-weight: 300;
    font-size: 46px;
    letter-spacing: 0.17em;
    color: var(--white);
    white-space: nowrap;
  }
  .launch-date {
    position: absolute;
    right: 24px; top: 288px;
    font-family: "Prata", serif;
    font-size: 17px;
    color: var(--white);
  }
  .headline { position: absolute; left: 0; top: 0; width: 848px; height: 1200px; }
  .headline text { fill: var(--cream); }
  .word-apartments { font-family: "Playfair Display", serif; font-weight: 600; font-size: 84px; filter: drop-shadow(0 4px 8px rgba(40,30,80,0.35)); }
  .word-new { font-family: "Playfair Display", serif; font-weight: 500; filter: drop-shadow(0 10px 18px rgba(40,30,80,0.45)); }
  .building-render { position: absolute; left: 0; top: 0; width: 848px; height: 1200px; }
  .developer-mark {
    position: absolute;
    left: 295px; top: 1040px;
    width: 284px; height: 160px;
    background: var(--white);
    display: flex; flex-direction: column; align-items: center; justify-content: center;
    font-family: "Montserrat", sans-serif;
    font-weight: 700;
    color: var(--ink);
  }
  .developer-name { font-size: 44px; line-height: 1; letter-spacing: -0.01em; }
  .developer-type { font-size: 17px; letter-spacing: 0.42em; margin-top: 14px; padding-left: 0.42em; }
</style>
</head>
<body>
<main class="banner">
  <div class="phase-mark"><span class="phase-name">Crest</span></div>
  <p class="project-name">Birchwell Landing</p>
  <p class="launch-date">Coming Spring 2022</p>

  <svg class="headline" viewBox="0 0 848 1200">
    <text class="word-apartments" x="14" y="387" textLength="814" lengthAdjust="spacing">APARTMENTS</text>
    <text class="word-new" x="0" y="905" font-size="700" textLength="848" lengthAdjust="spacingAndGlyphs">NEW</text>
  </svg>

  <svg class="building-render" viewBox="0 0 848 1200" role="img" aria-label="Architectural rendering of the new six-storey apartment building on a street corner">
    <defs>
      <linearGradient id="render-tone" x1="0" y1="0" x2="0" y2="1">
        <stop offset="0" stop-color="var(--render-light)" stop-opacity="0"/>
        <stop offset="0.3" stop-color="var(--render-light)" stop-opacity="0.95"/>
        <stop offset="0.65" stop-color="var(--render-mid)"/>
        <stop offset="1" stop-color="var(--render-dark)"/>
      </linearGradient>
    </defs>
    <rect x="0" y="760" width="848" height="440" fill="url(#render-tone)"/>
  </svg>

  <div class="developer-mark">
    <span class="developer-name">TOLVAR</span>
    <span class="developer-type">PROPERTIES</span>
  </div>
</main>
</body>
</html>
```